Counselling/ Wellness Clinic Needing Business Card & Matching Brochure

Looking for a brochure and business card that matches our brand, see logo and screen shots of our rebranding webpage.
We would like a QR code that takes to our website. The rebranding website that is not active will be lanternbrookcalming.ca
You we see we like depth, feeling through colours which has been through gradient. We want the brochure to show our services and make us stand out. The final design should match the website in a creative way.

```html
<!DOCTYPE html>
<html lang="en">
<head>
<meta charset="utf-8">
<title>Lanternbrook Calming Counselling – Trifold Brochure</title>
<link href="https://fonts.googleapis.com/css2?family=Montserrat:wght@400;600;700;800&family=Open+Sans:wght@400;600&family=Playfair+Display:ital,wght@1,700&display=swap" rel="stylesheet">
<style>
:root{
  --ink:#1f0b47;
  --deep:#2b0f62;
  --violet:#5a2aa8;
  --orchid:#8f45d6;
  --magenta:#b44fd8;
  --lilac:#d8c6f3;
  --mist:#f1eafb;
  --white:#ffffff;
  --bg:#ece8f1;
}
*{box-sizing:border-box;margin:0;padding:0}
html,body{width:784px;height:1200px;overflow:hidden}
body{background:var(--bg);font-family:"Open Sans",sans-serif;color:var(--white)}
.sheet{position:absolute;left:20px;width:744px;height:560px;display:flex;box-shadow:0 6px 18px rgba(31,11,71,.25)}
.sheet.outside{top:20px}
.sheet.inside{top:620px}
.panel{width:248px;height:100%;padding:22px 18px;position:relative;overflow:hidden}
.dark{background:linear-gradient(160deg,var(--deep) 0%,var(--violet) 60%,var(--orchid) 100%)}
.light{background:var(--white);color:var(--ink)}
.services{width:496px;background:linear-gradient(135deg,var(--deep),var(--violet) 55%,var(--orchid));display:grid;grid-template-columns:1fr 1fr;gap:14px;padding:22px 18px}
h2{font-family:"Montserrat",sans-serif;font-weight:800;font-size:22px;margin-bottom:12px}
h3{font-family:"Montserrat",sans-serif;font-weight:700;font-size:11px;margin-bottom:4px;color:var(--violet)}
p{font-size:8.5px;line-height:1.5}
.service-col{display:flex;flex-direction:column;gap:10px}
.service-grid{display:grid;grid-template-columns:1fr 1fr;gap:8px}
.service-box{background:var(--white);border-radius:6px;padding:8px;color:var(--ink)}
.service-box p{font-size:7.5px}
.service-box.wide{grid-column:span 2}
.tags{display:grid;grid-template-columns:1fr 1fr;gap:6px;margin-top:4px}
.tag{background:var(--mist);color:var(--violet);font-family:"Montserrat",sans-serif;font-weight:700;font-size:8px;text-align:center;padding:6px 4px;border-radius:4px}
.tag.solid{background:var(--magenta);color:var(--white)}
.cover{padding:0;background:var(--deep)}
.cover-top{background:linear-gradient(180deg,var(--white),var(--lilac));height:210px;padding:26px 18px;text-align:center;color:var(--ink)}
.brand{font-family:"Montserrat",sans-serif;font-weight:700;font-size:11px;color:var(--violet);letter-spacing:.5px;display:flex;align-items:center;justify-content:center;gap:6px}
.brand .dot{width:10px;height:10px;border-radius:50%;background:var(--orchid)}
.cover-title{font-family:"Playfair Display",serif;font-style:italic;font-weight:700;font-size:26px;line-height:1.1;margin:18px 0 8px;color:var(--violet)}
.cover-sub{font-size:9px;color:var(--ink)}
.art{position:absolute}
.art.brain{left:24px;top:270px;width:200px;height:200px;border-radius:50%;background:radial-gradient(circle,var(--magenta),var(--violet) 55%,transparent 72%)}
.art.wings{right:14px;top:226px;width:70px;height:60px;border-radius:12px;background:linear-gradient(135deg,var(--orchid),var(--lilac));opacity:.8}
.art.wings-low{left:16px;bottom:20px;width:70px;height:60px;border-radius:12px;background:linear-gradient(135deg,var(--lilac),var(--orchid));opacity:.7}
.art.team{left:18px;right:18px;bottom:22px;height:170px;border-radius:10px;background:linear-gradient(160deg,var(--lilac),var(--orchid))}
.art.wings-soft{right:16px;top:20px;width:70px;height:60px;border-radius:12px;background:linear-gradient(135deg,var(--lilac),var(--mist))}
.reasons{list-style:none;margin-top:4px}
.reasons li{display:flex;gap:8px;align-items:flex-start;font-size:8.5px;line-height:1.45;margin-bottom:9px}
.tick{flex:none;width:14px;height:14px}
.quote{background:linear-gradient(135deg,var(--violet),var(--orchid));color:var(--white);border-radius:8px;padding:10px 12px;margin-top:10px}
.quote .mark{font-family:"Playfair Display",serif;font-size:26px;line-height:.6;display:block;margin-bottom:4px}
.quote p{font-size:8.5px}
.back{text-align:center}
.back h2{font-size:20px;margin-top:16px}
.contact{list-style:none;text-align:left;margin:16px auto 0;width:180px}
.contact li{display:flex;gap:8px;align-items:center;font-size:9px;margin-bottom:10px}
.contact svg{width:14px;height:14px;flex:none}
.qr-block{display:flex;align-items:center;gap:12px;margin:10px auto 0;width:190px;text-align:left}
.qr-box{flex:none;width:74px;height:74px;background:var(--white);border-radius:6px;display:flex;align-items:center;justify-content:center;color:var(--violet);font-family:"Montserrat",sans-serif;font-weight:700;font-size:8px}
.qr-label{font-family:"Montserrat",sans-serif;font-weight:700;font-size:10px;line-height:1.3}
.note{margin-top:14px;background:rgba(255,255,255,.12);border-radius:8px;padding:10px}
</style>
</head>
<body>

<section class="sheet outside">
  <div class="services">
    <div class="service-col">
      <h2>Our Services</h2>
      <div class="service-grid">
        <div class="service-box"><h3>Individual Therapy</h3><p>One-on-one sessions shaped around your goals and pace.</p></div>
        <div class="service-box"><h3>Couples Counselling</h3><p>Rebuild trust and clear communication together.</p></div>
        <div class="service-box"><h3>Anxiety &amp; Stress</h3><p>Practical tools to calm the mind and body.</p></div>
        <div class="service-box"><h3>Grief Support</h3><p>Gentle care through loss and life change.</p></div>
      </div>
      <p>Our counsellors blend evidence-based methods with warm, steady support so every client feels heard, safe and guided toward lasting balance and growth.</p>
      <div class="tags"><span class="tag solid">In Person</span><span class="tag">Virtual</span><span class="tag">Family</span><span class="tag solid">Youth</span></div>
    </div>
    <div class="service-col">
      <div class="service-box wide"><h3>Trauma-Informed Care</h3><p>Safe, paced work that honours your story and your strengths as you heal.</p></div>
      <div class="service-grid">
        <div class="service-box"><h3>Mindfulness</h3><p>Grounding practice for daily calm.</p></div>
        <div class="service-box"><h3>Workshops</h3><p>Small group learning and skills.</p></div>
      </div>
      <div class="service-box wide"><h3>Life Transitions</h3><p>Support through new roles, moves, careers and relationships.</p></div>
      <div class="tags"><span class="tag">Book a Session</span><span class="tag solid">Free Consult</span></div>
    </div>
  </div>
  <div class="panel cover">
    <div class="cover-top">
      <div class="brand"><span class="dot"></span>Lanternbrook Calming</div>
      <div class="cover-title">Lanternbrook<br>Calming Counselling</div>
      <div class="cover-sub">Professional &amp; compassionate therapy</div>
    </div>
    <div class="art wings" role="img" aria-label="Flying butterflies illustration"></div>
    <div class="art brain" role="img" aria-label="Glowing purple brain illustration"></div>
    <div class="art wings-low" role="img" aria-label="Butterflies illustration"></div>
  </div>
</section>

<section class="sheet inside">
  <div class="panel dark">
    <h2>About Us</h2>
    <p>At Lanternbrook Calming Counselling we believe healing begins with feeling understood. Our team offers a calm, welcoming space where you can explore your thoughts and emotions without judgment.</p>
    <p style="margin-top:8px">Our counsellors bring years of training across anxiety, relationships, grief and trauma, meeting each person with patience and care.</p>
    <div class="art team" role="img" aria-label="Photo of the counselling team"></div>
  </div>
  <div class="panel light">
    <h2 style="color:var(--violet);font-size:19px">Why Work With Us?</h2>
    <ul class="reasons">
      <li><svg class="tick" viewBox="0 0 14 14"><circle cx="7" cy="7" r="7" fill="#8f45d6"/><path d="M4 7.2l2 2 4-4.4" stroke="#fff" stroke-width="1.6" fill="none"/></svg>We provide kind support for your family, teens and adults.</li>
      <li><svg class="tick" viewBox="0 0 14 14"><circle cx="7" cy="7" r="7" fill="#8f45d6"/><path d="M4 7.2l2 2 4-4.4" stroke="#fff" stroke-width="1.6" fill="none"/></svg>We offer flexible and virtual sessions.</li>
      <li><svg class="tick" viewBox="0 0 14 14"><circle cx="7" cy="7" r="7" fill="#8f45d6"/><path d="M4 7.2l2 2 4-4.4" stroke="#fff" stroke-width="1.6" fill="none"/></svg>We move with your needs and your pace.</li>
    </ul>
    <div class="quote"><span class="mark">“</span><p>Our goal is to help you feel lighter, clearer and more at home within yourself.</p></div>
    <div class="quote"><span class="mark">“</span><p>Every small step forward matters, and we walk each one beside you.</p></div>
  </div>
  <div class="panel dark back">
    <div class="art wings-soft" role="img" aria-label="Soft butterfly illustration"></div>
    <div class="brand" style="color:var(--white);margin-top:66px"><span class="dot"></span>Lanternbrook Calming</div>
    <h2>Let's Begin, Together</h2>
    <p>Reach out today to book your first session.</p>
    <ul class="contact">
      <li><svg viewBox="0 0 14 14"><path d="M3 1h3l1 3-2 1a7 7 0 0 0 4 4l1-2 3 1v3a1 1 0 0 1-1 1A11 11 0 0 1 2 2a1 1 0 0 1 1-1z" fill="#fff"/></svg>(647) 555-0182</li>
      <li><svg viewBox="0 0 14 14"><rect x="1" y="3" width="12" height="8" rx="1" fill="none" stroke="#fff" stroke-width="1.3"/><path d="M1.5 3.5L7 8l5.5-4.5" stroke="#fff" stroke-width="1.3" fill="none"/></svg>hello@lanternbrookcalming.ca</li>
      <li><svg viewBox="0 0 14 14"><circle cx="7" cy="7" r="6" fill="none" stroke="#fff" stroke-width="1.3"/><path d="M1 7h12M7 1c-3 3-3 9 0 12M7 1c3 3 3 9 0 12" stroke="#fff" stroke-width="1" fill="none"/></svg>lanternbrookcalming.ca</li>
    </ul>
    <div class="qr-block">
      <div class="qr-box" role="img" aria-label="QR code linking to lanternbrookcalming.ca">QR code</div>
      <div class="qr-label">Scan to visit<br>our website</div>
    </div>
    <div class="note"><p>Sessions available in person and online across the region.</p></div>
  </div>
</section>

</body>
</html>
```